Copper Ridge Excursions Post Card/Flyer

Postcard/flyer needs to convey our mission: to provide an authentic, boutique wine tour of exceptional quality with first class customer service. It needs to be clean and high quality. Less is more :) Worthy of 5 star hotel concierges handing them to a guest. I provided an old flyer my friend made and my competitors flyer. Please use these just as reference, but i want to see your creativity. I like the format of "Meadow Harvest" -scan 91-flyer BUT I don't want to copy.
Updates

Need extra days to review

Target Market(s)

Couples, travelers, hotel employees, local industry, etc...

Industry/Entity Type

Boutique

Requirements
Must have
• Must have bullet points of the my previous reference flyer and any photos .Please use website for reference too.
• Revulo, route scout affirmations Plus Snapmora
• "Group and Private Tours available"
• "Mention this card for 10% off any tour" - low key please
• copperridgeexcursions.com, info@copperridgeexcursions.com, 805-618-2934
Nice to have
• clean lines , simple and elegant
• double sided please
Should not have
• Not too busy.

```html
<!DOCTYPE html>
<html lang="en">
<head>
<meta charset="utf-8">
<title>Copper Ridge Excursions Postcard</title>
<link rel="stylesheet" href="https://fonts.googleapis.com/css2?family=Cinzel:wght@500&family=Noto+Serif:ital,wght@0,400;0,700;1,400;1,700&display=swap">
<style>
:root{
  --green:#1f6b3e;
  --green-bright:#2a9a45;
  --green-dark:#1b5e37;
  --tan:#d9b89a;
  --bronze-dark:#7a5a3e;
  --bronze-light:#e6bda2;
  --ink:#1d1d1d;
  --white:#ffffff;
  --stage:#d6d6d6;
}
*{box-sizing:border-box;margin:0;padding:0}
html,body{width:1149px;height:1200px;overflow:hidden}
body{background:var(--stage);position:relative;font-family:"Noto Serif",serif;color:var(--ink)}
.card{position:absolute;left:83px;width:796px;height:541px;background:var(--white);overflow:hidden;box-shadow:0 3px 8px rgba(0,0,0,.35)}
.card--front{top:36px}
.card--back{top:612px}
.abs{position:absolute}
.art{position:absolute;inset:0}
/* front */
.brand{left:0;top:0;width:290px;height:205px;display:flex;flex-direction:column;align-items:center;justify-content:center;gap:12px}
.brand__mark{width:18px;height:18px;background:var(--green)}
.brand__name{font-family:"Cinzel",serif;font-weight:500;color:var(--bronze-dark);font-size:22px;letter-spacing:1px;text-align:center;line-height:1.15}
.brand__region{font-family:"Cinzel",serif;font-size:9px;letter-spacing:3px;color:var(--green-dark)}
.headline{left:34px;top:226px;color:var(--white);font-weight:700;font-size:43px;line-height:42px}
.tagline{left:0;top:419px;width:796px;height:70px;display:flex;align-items:center;padding-left:35px;font-style:italic;font-size:31px}
.contact-bar{left:0;top:491px;width:796px;height:50px;background:linear-gradient(90deg,var(--bronze-dark),var(--bronze-light) 55%,var(--bronze-dark));display:flex;align-items:center;padding-left:36px;gap:8px;font-style:italic;font-weight:700;font-size:18.5px;white-space:nowrap}
.contact-bar svg{width:13px;height:13px;flex:none}
/* back */
.tours-title{left:14px;top:22px;width:430px;text-align:center;font-weight:700;line-height:1.05}
.tours-title__lead{color:var(--green);font-size:44px}
.tours-title__main{color:var(--ink);font-size:50px}
.tour-types{left:14px;top:136px;width:430px;text-align:center;font-size:20px;line-height:35px}
.dot{display:inline-block;width:9px;height:9px;border-radius:50%;background:var(--green);margin:0 5px 3px 12px;vertical-align:middle}
.benefits{left:22px;top:228px;width:375px;list-style:none;color:var(--white);font-weight:700;font-size:20px;line-height:25px}
.benefits li{position:relative;padding-left:18px;margin-bottom:7px}
.benefits li::before{content:"";position:absolute;left:0;top:10px;width:8px;height:8px;border-radius:50%;background:var(--tan)}
.offer{left:407px;top:220px;width:200px;text-align:center;color:var(--white);font-style:italic;white-space:nowrap}
.offer__intro{font-size:17px;line-height:23px;margin-top:48px}
.offer__value{font-size:35px;font-weight:700;color:var(--tan);line-height:40px}
.offer__tail{font-style:normal;font-size:28px;line-height:30px}
.call{left:22px;top:443px;font-style:italic;font-weight:700;color:var(--green-dark);font-size:32px;letter-spacing:4px}
.footer-bar{left:0;top:491px;width:463px;height:50px;background:linear-gradient(90deg,var(--bronze-dark),var(--bronze-light) 55%,var(--bronze-dark));display:flex;align-items:center;justify-content:space-between;padding:0 18px 0 22px;font-size:13px;white-space:nowrap}
</style>
</head>
<body>

<section class="card card--front">
  <svg class="art" viewBox="0 0 796 541">
    <defs>
      <linearGradient id="greenBand" x1="0" x2="1">
        <stop offset="0" stop-color="#1b5e37"/><stop offset=".6" stop-color="#2a9a45"/><stop offset="1" stop-color="#1f6b3e"/>
      </linearGradient>
      <linearGradient id="vineyard" x1="0" y1="0" x2="0" y2="1">
        <stop offset="0" stop-color="#9cc6ea"/><stop offset=".38" stop-color="#cfe3f1"/><stop offset=".42" stop-color="#8a5a36"/><stop offset=".7" stop-color="#8b8a2e"/><stop offset="1" stop-color="#5a4a24"/>
      </linearGradient>
    </defs>
    <polygon points="0,205 330,205 332,210 0,210" fill="#d9b89a"/>
    <polygon points="0,214 340,214 435,412 0,412" fill="url(#greenBand)"/>
    <polygon points="242,40 250,40 340,210 332,210" fill="#d9b89a"/>
    <polygon points="250,0 262,0 442,402 430,402" fill="#1f6b3e"/>
    <polygon role="img" aria-label="Photo of rolling vineyard rows in autumn under a clear sky" points="262,0 796,0 796,402 442,402" fill="url(#vineyard)"/>
    <rect x="0" y="402" width="796" height="8" fill="#1f6b3e"/>
    <rect x="0" y="412" width="796" height="7" fill="#d9b89a"/>
  </svg>
  <div class="abs brand">
    <span class="brand__mark"></span>
    <div class="brand__name">Copper Ridge<br>Excursions</div>
    <div class="brand__region">SANTA BARBARA COUNTY</div>
  </div>
  <h1 class="abs headline">Come explore<br>santa barbara<br>wine country<br>with us!</h1>
  <p class="abs tagline">An authentic and boutique wine tour experience.</p>
  <div class="abs contact-bar">
    <span>Contact us for availability</span>
    <svg viewBox="0 0 14 14" aria-hidden="true"><path d="M3 1 L5 1 L6 4 L4.5 5 Q6 8.5 9 9.5 L10 8 L13 9 L13 11 Q12 13 10 13 Q2 11 1 3 Q1 1 3 1Z" fill="#f3e6da"/></svg>
    <span>(805)618-2934</span>
    <svg viewBox="0 0 14 14" aria-hidden="true"><circle cx="7" cy="7" r="6" fill="none" stroke="#f3e6da" stroke-width="1.4"/><path d="M1 7H13M7 1V13M3 3.5Q7 6 11 3.5M3 10.5Q7 8 11 10.5" stroke="#f3e6da" stroke-width="1" fill="none"/></svg>
    <span>copperridgeexcursions.com</span>
  </div>
</section>

<section class="card card--back">
  <svg class="art" viewBox="0 0 796 541">
    <defs>
      <linearGradient id="greenPanel" x1="0" x2="1">
        <stop offset="0" stop-color="#1b5e37"/><stop offset=".55" stop-color="#2a9a45"/><stop offset="1" stop-color="#1f6b3e"/>
      </linearGradient>
      <radialGradient id="badge" cx=".5" cy=".4" r=".6">
        <stop offset="0" stop-color="#2a9a45"/><stop offset="1" stop-color="#1b5e37"/>
      </radialGradient>
      <linearGradient id="group" x1="0" y1="0" x2="0" y2="1">
        <stop offset="0" stop-color="#b8d4ea"/><stop offset=".3" stop-color="#7f9a6a"/><stop offset=".65" stop-color="#8a7a6a"/><stop offset="1" stop-color="#3b4a68"/>
      </linearGradient>
      <linearGradient id="lake" x1="0" y1="0" x2="0" y2="1">
        <stop offset="0" stop-color="#4f7a3a"/><stop offset=".6" stop-color="#6e8fa0"/><stop offset="1" stop-color="#8a9fb0"/>
      </linearGradient>
      <linearGradient id="cellar" x1="0" y1="0" x2="0" y2="1">
        <stop offset="0" stop-color="#c9822e"/><stop offset=".5" stop-color="#7a4a22"/><stop offset="1" stop-color="#6e7fa0"/>
      </linearGradient>
    </defs>
    <rect x="0" y="213" width="463" height="6" fill="#d9b89a"/>
    <rect x="0" y="221" width="463" height="202" fill="url(#greenPanel)"/>
    <rect x="0" y="423" width="463" height="8" fill="#d9b89a"/>
    <rect x="463" y="0" width="8" height="541" fill="#d9b89a"/>
    <rect x="471" y="0" width="6" height="541" fill="#1f6b3e"/>
    <rect role="img" aria-label="Photo of a group of friends toasting with wine at a vineyard" x="477" y="0" width="319" height="305" fill="url(#group)"/>
    <rect x="477" y="305" width="319" height="5" fill="#1f6b3e"/>
    <rect role="img" aria-label="Photo of guests raising glasses beside a vineyard pond" x="477" y="310" width="157" height="231" fill="url(#lake)"/>
    <rect x="634" y="310" width="5" height="231" fill="#1f6b3e"/>
    <rect role="img" aria-label="Photo of a tour group inside a candlelit wine cave" x="639" y="310" width="157" height="231" fill="url(#cellar)"/>
    <circle cx="507" cy="313" r="107" fill="#d9b89a"/>
    <circle cx="507" cy="313" r="99" fill="url(#badge)"/>
  </svg>
  <h2 class="abs tours-title"><span class="tours-title__lead">Group and Private</span><br><span class="tours-title__main">Tours available</span></h2>
  <p class="abs tour-types"><span class="dot"></span>Group Tours <span class="dot"></span>Private Tours<br><span class="dot"></span>Special Tours</p>
  <ul class="abs benefits">
    <li>Premium wine tasting at boutique wineries</li>
    <li>Safe and comfortable luxury<br>vehicles</li>
    <li>Picnic lunch in a vineyard setting</li>
    <li>Local expert guides</li>
  </ul>
  <div class="abs offer">
    <p class="offer__intro">Mention Harbor Notes<br>for</p>
    <p class="offer__value">10% off</p>
    <p class="offer__tail">any tour</p>
  </div>
  <p class="abs call">CALL US 805-618-2934</p>
  <div class="abs footer-bar">
    <span>info@copperridgeexcursions.com</span>
    <span>copperridgeexcursions.com</span>
  </div>
</section>

</body>
</html>
```